Velmo Online Company needs Trendy Advertising Posters

We need 6 x posters designer:
We have some quotes that we'd like to be designed to be used for online posters, advertising an online business. We need text posters designed for all of the content provided , please send over many designs for us to choose from - each poster will look different from the others. The more examples you provide the better.

Each poster will contain a large, bold, powerful quote - with 'graffiti style' corrections over some words. For example: a vandalised poster with a word replaced with spray paint style font.

Quotes/content and examples provided. The examples we’ve provided are not fixed in terms of colour and layout etc. Creative input would be useful.

Colours/general theme to be similar to: www.velmo.uk

Font styles to use
Serif
Sans Serif
Decorative

Colors
0493ce
33a6d7
85cae6
cee9f5
f9d9e8
eea4c8
e667a6
e34197
0555a3

Requirements
Must have
• Graffiti style font.
Nice to have
• Many designs to choose from.

```html
<!DOCTYPE html>
<html lang="en">
<head>
<meta charset="utf-8">
<title>Velmo — Poster Series</title>
<link href="https://fonts.googleapis.com/css2?family=Bungee&family=Caveat&family=Jura:wght@300;400;500&display=swap" rel="stylesheet">
<style>
  :root{
    --canvas:#f2f2f4;
    --ink:#000;
    --paper:#fff;
    --red:#ec1c24;
    --blue:#00a0e3;
    --green:#8dc63f;
    --orange:#f7941d;
    --teal:#1ba39c;
    --purple:#662d91;
    --purple-text:#8a48c0;
    --brown:#c0703f;
  }
  *{margin:0;padding:0;box-sizing:border-box}
  html,body{width:1200px;height:1193px;overflow:hidden;background:var(--canvas)}
  .series{position:relative;width:1200px;height:1193px}
  .poster{position:absolute;width:295px;height:456px;background:var(--ink);color:var(--paper);overflow:hidden}
  .col-1{left:143px}.col-2{left:452px}.col-3{left:761px}
  .row-1{top:133px}.row-2{top:603px}

  .quote-mark{position:absolute;font-family:"Bungee",sans-serif;font-size:58px;line-height:1;height:30px;overflow:hidden}
  .quote-mark span{display:block;margin-top:-6px}

  .bold{font-family:"Bungee",sans-serif;color:var(--paper)}
  .outline{font-family:"Bungee",sans-serif;color:transparent;-webkit-text-stroke:1.1px var(--paper)}
  .thin{font-family:"Jura",sans-serif;font-weight:300}
  .script{font-family:"Caveat",cursive;font-size:13px;line-height:13px;position:absolute;white-space:nowrap}

  .lines{position:absolute;white-space:nowrap}
  .lines p{margin:0}

  .footer{position:absolute;left:32px;top:400px;display:flex;align-items:center}
  .brand{font-family:"Bungee",sans-serif;font-size:15px;color:var(--paper);width:83px;letter-spacing:.3px}
  .divider{width:1px;height:28px;background:var(--paper);opacity:.8;margin-right:25px}
  .tagline{font-family:"Jura",sans-serif;font-weight:500;font-size:6px;line-height:8px;letter-spacing:1.3px;text-transform:uppercase}

  .strike{position:absolute;pointer-events:none}

  /* poster 1 */
  .p1 .walls{left:31px;top:92px;font-size:29px;line-height:33px}
  .p1 .people{right:30px;top:216px;font-size:29px;line-height:33px;text-align:right}
  .p1 .fix{left:32px;top:254px;color:var(--red)}

  /* poster 2 */
  .p2 .lines{left:30px;top:100px;font-size:29px;line-height:32.4px}

  /* poster 3 */
  .p3 .lines{left:33px;top:102px;font-size:19px;line-height:29.8px;letter-spacing:6.5px}

  /* poster 4 */
  .p4 .lines{left:31px;top:95px;font-size:29px;line-height:30.4px}
  .p4 .fix{color:var(--orange)}

  /* poster 5 */
  .p5 .quote-mark{left:50%;transform:translateX(-50%)}
  .p5 .calling{left:0;right:0;top:77px;text-align:center;font-size:52px;line-height:53px}
  .p5 .trades{position:absolute;left:0;right:0;top:340px;text-align:center;font-family:"Jura",sans-serif;font-size:6.5px;line-height:9px;letter-spacing:1.1px;text-transform:uppercase}

  /* poster 6 */
  .p6 .column{position:absolute;top:46px;display:flex;flex-direction:column;align-items:center;width:20px;font-family:"Jura",sans-serif;font-weight:400;font-size:20px;line-height:25.5px}
  .p6 .column span{display:block;height:25.5px}
  .p6 .column .gap{height:7px}
  .p6 .accent{color:var(--purple-text)}
  .p6 .fix{left:168px;top:350px;color:var(--paper)}
</style>
</head>
<body>
<main class="series">

  <!-- Poster 1 -->
  <section class="poster p1 col-1 row-1">
    <div class="quote-mark" style="left:30px;top:45px;color:var(--red)"><span>“</span></div>
    <div class="lines outline walls"><p>IT’S NOT</p><p>WALLS THAT</p><p>MAKE THE</p><p>CITY</p></div>
    <div class="lines bold people"><p>IT’S THE</p><p>PEOPLE THAT</p><p>LIVE WITHIN</p><p>THEM</p></div>
    <div class="script fix">DEVELOPERS</div>
    <svg class="strike" style="left:48px;top:268px" width="130" height="20" viewBox="0 0 130 20"><path d="M2 6 L126 14 M8 9 L128 17" stroke="var(--red)" stroke-width="3" stroke-linecap="round" fill="none"/></svg>
    <div class="footer"><span class="brand">Velmo</span><span class="divider"></span><p class="tagline" style="color:var(--brown)">Sign up for the leading<br>business directory for the<br>UK property industry</p></div>
  </section>

  <!-- Poster 2 -->
  <section class="poster p2 col-2 row-1">
    <div class="quote-mark" style="left:30px;top:53px;color:var(--blue)"><span>“</span></div>
    <div class="lines bold"><p>MAYBE IT’S</p><p>BECAUSE</p><p>I’M A</p><p>LONDONER</p><p>PLANNING</p><p>CONSULTANT</p></div>
    <div class="footer" style="top:408px"><span class="brand">Velmo</span><span class="divider"></span><p class="tagline" style="color:var(--blue)">Sign up for the leading<br>business directory for the<br>UK property industry</p></div>
  </section>

  <!-- Poster 3 -->
  <section class="poster p3 col-3 row-1">
    <div class="quote-mark" style="left:30px;top:53px;color:var(--green)"><span>“</span></div>
    <div class="lines thin"><p>...OR MAYBE</p><p>IT’S BECAUSE</p><p>I’M A</p><p>LONDONER</p><p>THAT I LOVE</p><p>LONDON TOWN</p><p>AND COUNTRY</p><p>PLANNING..</p></div>
    <div class="footer" style="top:408px"><span class="brand">Velmo</span><span class="divider"></span><p class="tagline" style="color:var(--green)">Sign up for the leading<br>business directory for the<br>UK property industry</p></div>
  </section>

  <!-- Poster 4 -->
  <section class="poster p4 col-1 row-2">
    <div class="quote-mark" style="left:30px;top:44px;color:var(--orange)"><span>“</span></div>
    <div class="lines"><p class="outline">A BAD DAY</p><p class="outline">IN LONDON</p><p class="outline">IS STILL</p><p><span class="outline">BETTER</span> <span class="bold">THAN</span></p><p class="bold">A GOOD DAY</p><p class="bold">ANYWHERE</p><p class="bold">ELSE</p></div>
    <svg class="strike" style="left:136px;top:102px" width="80" height="18" viewBox="0 0 80 18"><path d="M2 14 C22 6 50 4 76 8 M8 15 L72 11" stroke="var(--orange)" stroke-width="3" stroke-linecap="round" fill="none"/></svg>
    <svg class="strike" style="left:140px;top:223px" width="70" height="18" viewBox="0 0 70 18"><path d="M2 14 C22 8 45 5 67 4 M8 15 L65 8" stroke="var(--orange)" stroke-width="3" stroke-linecap="round" fill="none"/></svg>
    <div class="script fix" style="left:216px;top:98px">Planning<br>Committe</div>
    <div class="script fix" style="left:210px;top:221px">Planning<br>Committe</div>
    <div class="footer"><span class="brand">Velmo</span><span class="divider"></span><p class="tagline" style="color:var(--orange)">Sign up for the leading<br>business directory for the<br>UK property industry</p></div>
  </section>

  <!-- Poster 5 -->
  <section class="poster p5 col-2 row-2">
    <div class="quote-mark" style="top:42px;color:var(--teal)"><span>“</span></div>
    <div class="lines calling"><p class="bold">LON</p><p class="bold">DON’S</p><p class="outline">CALL</p><p class="outline">ING..</p></div>
    <div class="quote-mark" style="top:297px;color:var(--teal)"><span>”</span></div>
    <p class="trades">(...for planning consultants<br>surveyors, architects, agents,<br>developers, builders, estate<br>agents, housing associations,<br>solicitors...)</p>
    <div class="footer" style="top:408px"><span class="brand">Velmo</span><span class="divider"></span><p class="tagline" style="color:var(--teal)">Sign up for the leading<br>business directory for the<br>UK property industry</p></div>
  </section>

  <!-- Poster 6 -->
  <section class="poster p6 col-3 row-2">
    <div class="quote-mark" style="left:30px;top:44px;color:var(--purple)"><span>“</span></div>
    <p class="column" style="left:94px" aria-label="A man who can"><span>A</span><span class="gap"></span><span>M</span><span>A</span><span>N</span><span class="gap"></span><span>W</span><span>H</span><span>O</span><span class="gap"></span><span>C</span><span>A</span><span>N</span></p>
    <p class="column accent" style="left:127px" aria-label="dominate"><span>D</span><span>O</span><span>M</span><span>I</span><span>N</span><span>A</span><span>T</span><span>E</span></p>
    <p class="column" style="left:158px" aria-label="a London"><span>A</span><span class="gap"></span><span>L</span><span>O</span><span>N</span><span>D</span><span>O</span><span>N</span></p>
    <p class="column" style="left:188px" aria-label="dinnertable"><span>D</span><span>I</span><span>N</span><span>N</span><span>E</span><span>R</span><span>T</span><span>A</span><span>B</span><span>L</span><span>E</span></p>
    <p class="column" style="left:219px" aria-label="can dominate"><span>C</span><span>A</span><span>N</span><span class="gap"></span><span>D</span><span>O</span><span>M</span><span>I</span><span>N</span><span>A</span><span>T</span><span>E</span></p>
    <p class="column accent" style="left:250px" aria-label="the world"><span>T</span><span>H</span><span>E</span><span class="gap"></span><span>W</span><span>O</span><span>R</span><span>L</span><span>D</span></p>
    <svg class="strike" style="left:188px;top:36px" width="20" height="312" viewBox="0 0 20 312"><path d="M10 0 L10 296" stroke="var(--purple-text)" stroke-width="2.5" fill="none"/><path d="M3 288 L10 310 L17 288 Z" fill="var(--purple-text)"/></svg>
    <div class="script fix">Planning<br>Committe</div>
    <div class="footer"><span class="brand">Velmo</span><span class="divider"></span><p class="tagline" style="color:var(--purple-text)">Sign up for the leading<br>business directory for the<br>UK property industry</p></div>
  </section>

</main>
</body>
</html>
```